Home Improvements Website

I would like a website that matches our business colour scheme and uses the fonts consistent without logo. (Monserrat, Chosence & Big Noddle Tiling).
We will need numerous sections: homepage, about us, services (with tiles or links to each service - building, landscaping, decking, maintenance, roofing, gutters etc) current projects (which must be easily editable by me, who is not too tech savvy) and a contacts page with enquiry form we can link to our job management service (Tradify).

```html
<!DOCTYPE html>
<html lang="en">
<head>
<meta charset="utf-8">
<title>Halvern Home Improvements</title>
<link href="https://fonts.googleapis.com/css2?family=Montserrat:wght@300;400;500&display=swap" rel="stylesheet">
<style>
  :root {
    --dark: #212529;
    --nav-link: rgba(255,255,255,0.55);
    --green: #008000;
    --light-green: #90ee90;
    --text: #212529;
    --white: #ffffff;
  }
  * { box-sizing: border-box; margin: 0; padding: 0; }
  html, body { width: 1200px; height: 826px; overflow: hidden; }
  body { font-family: "Montserrat", sans-serif; color: var(--text); background: var(--white); }
  .container { width: 808px; margin: 0 auto; }

  .site-nav { height: 66px; background: var(--dark); }
  .site-nav .container { height: 100%; display: flex; align-items: center; justify-content: space-between; }
  .brand { display: flex; align-items: center; gap: 6px; color: var(--white); font-size: 12px; font-weight: 500; }
  .brand-dot { width: 10px; height: 10px; border-radius: 50%; background: var(--green); }
  .nav-links { display: flex; gap: 10px; list-style: none; }
  .nav-links a { color: var(--nav-link); text-decoration: none; font-size: 10.5px; }

  .hero { position: relative; height: 250px; display: flex; flex-direction: column; align-items: center; justify-content: center; text-align: center; color: var(--white); }
  .hero-photo { position: absolute; inset: 0; background: linear-gradient(90deg, #5d5d5d 0%, #6f6f6f 45%, #7a6a5a 75%, #6a5544 100%); }
  .hero-content { position: relative; }
  .hero h1 { font-size: 27px; font-weight: 400; line-height: 1.2; }
  .hero p { font-size: 10px; margin-top: 2px; }
  .btn { display: inline-block; background: var(--green); color: var(--white); font-size: 10.5px; padding: 5px 8px; border-radius: 3px; text-decoration: none; }
  .hero .btn { margin-top: 3px; }

  .service-strip { height: 129px; padding-top: 29px; }
  .service-strip .container { display: flex; gap: 16px; }
  .service { flex: 1; text-align: center; }
  .service h2 { font-size: 19px; font-weight: 400; }
  .service p { font-size: 10px; font-weight: 300; line-height: 15px; margin-top: 6px; }

  .featured { height: 336px; background: var(--light-green); padding-top: 28px; }
  .featured h2 { font-size: 21px; font-weight: 400; text-align: center; line-height: 1; }
  .project-grid { display: flex; gap: 17px; align-items: flex-start; margin-top: 9px; }
  .project-card { width: 258px; background: var(--white); border-radius: 4px; overflow: hidden; }
  .project-photo { height: 125px; }
  .photo-bedroom { background: linear-gradient(135deg, #9c8c78, #d8d6d2); }
  .photo-kitchen { background: linear-gradient(90deg, #a88a6a, #dcdad6 60%, #4f6a3e); }
  .photo-deck { background: linear-gradient(180deg, #2f3a22 0%, #5a4530 55%, #8a5a38 100%); }
  .project-body { padding: 10px 10px 10px; }
  .project-body h3 { font-size: 13.5px; font-weight: 400; }
  .project-body p { font-size: 10px; font-weight: 300; line-height: 15px; margin: 4px 0 10px; }

  .site-footer { height: 45px; background: var(--dark); color: var(--white); font-size: 10.5px; display: flex; align-items: center; justify-content: center; }
</style>
</head>
<body>
  <nav class="site-nav">
    <div class="container">
      <div class="brand"><span class="brand-dot"></span>Halvern</div>
      <ul class="nav-links">
        <li><a href="#">Home</a></li>
        <li><a href="#">About Us</a></li>
        <li><a href="#">Services</a></li>
        <li><a href="#">Current Projects</a></li>
        <li><a href="#">Contact Us</a></li>
      </ul>
    </div>
  </nav>

  <header class="hero">
    <div class="hero-photo" role="img" aria-label="Wooden step ladder leaning against a freshly painted grey wall"></div>
    <div class="hero-content">
      <h1>Welcome to Halvern Home Improvements</h1>
      <p>Your trusted partner in home improvement services.</p>
      <a class="btn" href="#">Our Services</a>
    </div>
  </header>

  <section class="service-strip">
    <div class="container">
      <div class="service"><h2>Building</h2><p>Professional building services for all your needs.</p></div>
      <div class="service"><h2>Landscaping</h2><p>Transforming outdoor spaces into beautiful landscapes.</p></div>
      <div class="service"><h2>Decking</h2><p>High-quality decking services to enhance your home.</p></div>
    </div>
  </section>

  <section class="featured">
    <div class="container">
      <h2>Featured Projects</h2>
      <div class="project-grid">
        <article class="project-card">
          <div class="project-photo photo-bedroom" role="img" aria-label="Modern bedroom with wood panelled wall and grey bedding"></div>
          <div class="project-body">
            <h3>Modern Living Room</h3>
            <p>A stylish renovation of a living room, featuring modern design elements and high-quality finishes.</p>
            <a class="btn" href="#">View Details</a>
          </div>
        </article>
        <article class="project-card">
          <div class="project-photo photo-kitchen" role="img" aria-label="Bright kitchen with wooden cabinets and plant wall"></div>
          <div class="project-body">
            <h3>Elegant Kitchen Remodel</h3>
            <p>Transforming kitchens into elegant, functional spaces with top-of-the-line appliances and fixtures.</p>
            <a class="btn" href="#">View Details</a>
          </div>
        </article>
        <article class="project-card">
          <div class="project-photo photo-deck" role="img" aria-label="Metal jug with dried flowers on a wooden deck table"></div>
          <div class="project-body">
            <h3>Beautiful Outdoor Deck</h3>
            <p>Creating stunning outdoor decks perfect for relaxing and entertaining guests.</p>
            <a class="btn" href="#">View Details</a>
          </div>
        </article>
      </div>
    </div>
  </section>

  <footer class="site-footer">© 2024 Halvern Home Improvements. All rights reserved.</footer>
</body>
</html>
```